Letterhead for Business Law Firm

We need a letter head for our firm based on the design we have settled on and it is attached. Our clients are small and large businesses around the world, and our letterhead is used typically for formal legal purposes such as demand letters (accusing the recipient of doing bad things) or responding to demand letters. It may also be sent to regulators and other government agencies. So this needs to be tasteful, but a little edgy as well - we try to convey that we are a firm that is different - businesses and investors come to us for creative, quick advice, typically in high stress circumstances, and for our ability to work through high conflict situations, and rapid paced engagements.

Target Market(s)

Lawyers, business executives, investors, government regulators who may receive letters from this firm on behalf of its clients.

Industry/Entity Type

Business

Requirements
Must have
• The design and the firm's contact information:
• Thornvale Law Firm, P.C.
• 8172 SW 17th Ave
• Portland, OR 97058
• phone: 971 555 0147
• fax: 971 555 0182
• in what placement and how depicted (e.g. a phone icon instead of the word "phone") I leave to your creative ideas.
Nice to have
• design and information can be placed at the top, bottom and/or sides of the letter, and the design should be for a standard letter size paper - and can have a separate design for the second page.

```html
<!DOCTYPE html>
<html lang="en">
<head>
<meta charset="utf-8">
<title>Thornvale Law Firm, P.C. — Letterhead</title>
<link rel="stylesheet" href="https://fonts.googleapis.com/css2?family=Michroma&display=swap">
<style>
  :root {
    --paper: #f2f2f2;
    --ink: #1a1414;
    --footer-band: #98b4bd;
    --rule: #4a4f52;
    --icon: #2a2a2a;
    --accent-green: #7cc242;
    --building-tone: #5d6a6f;
  }
  * { margin: 0; padding: 0; box-sizing: border-box; }
  html, body { width: 867px; height: 1200px; overflow: hidden; background: var(--paper); }
  .letterhead {
    position: relative;
    width: 867px;
    height: 1200px;
    background: var(--paper);
    font-family: "Michroma", sans-serif;
  }
  .masthead {
    position: absolute;
    left: 133px;
    top: 26px;
    width: 621px;
    height: 102px;
    display: flex;
    align-items: center;
    justify-content: center;
  }
  .firm-name {
    font-weight: 400;
    font-size: 30px;
    letter-spacing: 0.42em;
    padding-left: 0.42em;
    color: var(--ink);
    white-space: nowrap;
  }
  .contact-band {
    position: absolute;
    left: 0;
    top: 1071px;
    width: 867px;
    height: 129px;
    background: var(--footer-band);
    color: var(--ink);
    font-size: 10.5px;
    line-height: 1.7;
  }
  .divider {
    position: absolute;
    top: 17px;
    width: 1px;
    height: 93px;
    background: var(--rule);
  }
  .divider--first { left: 266px; }
  .divider--second { left: 627px; }
  .building-mark {
    position: absolute;
    left: 15px;
    top: 17px;
    width: 18px;
    height: 86px;
    background: linear-gradient(180deg, var(--building-tone), var(--icon));
  }
  .icon { position: absolute; }
  .icon--mail { left: 289px; top: 26px; }
  .icon--web { left: 291px; top: 78px; }
  .icon--phone { left: 644px; top: 20px; }
  .icon--fax { left: 642px; top: 77px; }
  .contact-text {
    position: absolute;
    font-style: normal;
    white-space: nowrap;
  }
  .address { left: 50px; top: 36px; }
  .email { left: 322px; top: 26px; }
  .website { left: 322px; top: 78px; }
  .phone { left: 672px; top: 24px; }
  .fax { left: 672px; top: 78px; }
</style>
</head>
<body>
  <main class="letterhead">
    <header class="masthead">
      <h1 class="firm-name">THORNVALE</h1>
    </header>

    <footer class="contact-band">
      <div class="building-mark" role="img" aria-label="Office building mark"></div>
      <address class="contact-text address">Thornvale Law Firm, P.C.<br>8172 SW 17th Ave<br>Portland, OR 97058</address>

      <span class="divider divider--first"></span>

      <svg class="icon icon--mail" width="22" height="18" viewBox="0 0 22 18" aria-hidden="true">
        <rect x="1" y="1" width="20" height="16" fill="none" stroke="var(--icon)" stroke-width="2"/>
        <path d="M1 1 L11 10 L21 1 M1 17 L8 8 M21 17 L14 8" fill="none" stroke="var(--icon)" stroke-width="1.6"/>
      </svg>
      <span class="contact-text email">office@thornvalelaw.com</span>

      <svg class="icon icon--web" width="20" height="20" viewBox="0 0 20 20" aria-hidden="true">
        <circle cx="9" cy="9" r="8" fill="var(--icon)"/>
        <path d="M1 9 H17 M9 1 V17 M3 5 H15 M3 13 H15" stroke="var(--footer-band)" stroke-width="1"/>
        <ellipse cx="9" cy="9" rx="4" ry="8" fill="none" stroke="var(--footer-band)" stroke-width="1"/>
        <rect x="11" y="11" width="7" height="8" fill="var(--accent-green)"/>
      </svg>
      <span class="contact-text website">www.thornvalelaw.com</span>

      <span class="divider divider--second"></span>

      <svg class="icon icon--phone" width="14" height="24" viewBox="0 0 14 24" aria-hidden="true">
        <rect x="3" y="0" width="3" height="6" fill="var(--icon)"/>
        <rect x="1" y="5" width="12" height="18" rx="3" fill="var(--icon)"/>
        <rect x="4" y="8" width="6" height="4" fill="var(--footer-band)"/>
        <circle cx="7" cy="17" r="2.2" fill="var(--footer-band)"/>
      </svg>
      <span class="contact-text phone">971 555 0147</span>

      <svg class="icon icon--fax" width="20" height="20" viewBox="0 0 20 20" aria-hidden="true">
        <rect x="5" y="1" width="10" height="7" fill="none" stroke="var(--icon)" stroke-width="1.8"/>
        <rect x="1" y="8" width="18" height="8" rx="2" fill="none" stroke="var(--icon)" stroke-width="1.8"/>
        <rect x="5" y="13" width="10" height="6" fill="var(--footer-band)" stroke="var(--icon)" stroke-width="1.8"/>
      </svg>
      <span class="contact-text fax">971 555 0182</span>
    </footer>
  </main>
</body>
</html>
```